依頼詳細
法人向け新サービスのダイレクトメール(はがきサイズ)を制作しますので、オフセット印刷入稿用デザインをお願い致します。

表は宛名印刷用ですので、下4分の一程度のデザイン(単色1c)、裏は全面デザイン(4c)をお願いします。

アウトドア用品の会社ですが、今回は法人向けDMですので、目を引くデザインを求めます。

・テンプレート(win・mac)用添付いたします。
・テキストは添付のとおりですが、デザイン・文字級数含め、レイアウトなどは、自由にご提案ください。
・写真画像は添付しますが、カンプ用のダミーですので、発注者が決まり次第、本番用の写真をお渡しします。
記載項目
テキストは添付ファイルの通りです。
希望イメージ
シンプル 複雑
単色 カラフル
暗い 明るい
日常 高級
遊び心 厳粛
未来的 伝統的
女性的 男性的
希望する色
水色系、茶系、緑系、黄・オレンジ系、色味などは弊社HPなども参考にしてください。さわやかな青系なども可です。
納品ファイル
• 高解像度JPG (.jpg)
• イラストレーター形式 (.ai)
補足説明
■ 選んだ理由

法人向けという堅い部分とアウトドア用品という柔らかさのバランス、見出しや文字級数の強弱のつけ方、DMという特性上、ぱっと見で入ってくる印象などで決定させていただきました。

■ 提案者全員のお礼・コメント

沢山のご提案ありがとうございました。
皆様それぞれに良い部分がありましたが、上記の部分を踏まえて、決定させていただきました。
またご機会がありましたら、何卒宜しくお願い申し上げます。

```html
<!DOCTYPE html>
<html lang="ja">
<head>
<meta charset="utf-8">
<title>アウトドア用品 年間定額レンタル 法人会員募集</title>
<link href="https://fonts.googleapis.com/css2?family=M+PLUS+Rounded+1c:wght@500;700;800;900&family=Noto+Sans+JP:wght@500;700;900&display=swap" rel="stylesheet">
<style>
  :root {
    --sky: #cfeefb;
    --navy: #1d3f8f;
    --green: #2f9a3a;
    --green-dark: #1f6b2a;
    --green-deep: #0e4a1c;
    --red: #e8342b;
    --yellow: #ffe94a;
    --lime: #e6f36a;
    --white: #ffffff;
    --ink: #2a2a2a;
  }
  * { margin: 0; padding: 0; box-sizing: border-box; }
  html, body { width: 811px; height: 1200px; overflow: hidden; background: var(--white); }
  body { font-family: "M PLUS Rounded 1c", "Noto Sans JP", sans-serif; color: var(--ink); }
  .card { position: relative; width: 811px; height: 1200px; overflow: hidden; background: var(--white); }

  /* header */
  .header { position: absolute; left: 0; top: 0; width: 811px; height: 170px;
    background: linear-gradient(180deg, var(--sky) 0%, #e9f8fe 100%); text-align: center; padding-top: 18px; }
  .price-line { font-weight: 900; color: var(--navy); font-size: 44px; letter-spacing: 1px; line-height: 1.1; white-space: nowrap; }
  .price-line .amount { font-size: 58px; }
  .price-line .course { display: inline-block; background: var(--navy); color: var(--white);
    font-size: 26px; padding: 4px 12px; border-radius: 8px; vertical-align: 10px; margin: 0 6px; }
  .headline { margin-top: 10px; font-weight: 900; font-size: 46px; color: var(--navy); line-height: 1.1; white-space: nowrap; }
  .headline span { background: linear-gradient(transparent 55%, var(--lime) 55%); }

  /* photo collage */
  .photo { position: absolute; }
  .photo-camp { left: 0; top: 170px; width: 262px; height: 330px;
    background: linear-gradient(160deg, #8fb6c9 0%, #c9b48a 55%, #6f7c4a 100%); }
  .photo-climb { left: 262px; top: 170px; width: 280px; height: 310px;
    background: linear-gradient(180deg, #4f8fd6 0%, #a9c9ea 50%, #e8eef4 75%, #8a8f96 100%); }
  .photo-bbq { left: 542px; top: 170px; width: 269px; height: 330px;
    background: linear-gradient(150deg, #6b3a1e 0%, #b8743c 45%, #3a2418 100%); }

  .bubble { position: absolute; background: var(--red); color: var(--white); font-weight: 900;
    border-radius: 40px; padding: 8px 22px; font-size: 30px; border: 4px solid var(--white); white-space: nowrap; }
  .bubble-camp { left: 22px; top: 188px; }
  .bubble-bbq { left: 548px; top: 186px; text-align: center; line-height: 1.1; font-size: 26px; padding: 8px 16px; }
  .bubble-bbq small { display: block; font-size: 14px; font-weight: 700; }
  .bubble-climb { left: 312px; top: 360px; }

  .main-copy { position: absolute; left: 0; top: 470px; width: 811px; text-align: center;
    font-weight: 900; font-size: 48px; line-height: 1.25; color: var(--green-deep); white-space: nowrap;
    -webkit-text-stroke: 12px var(--white); paint-order: stroke fill; }

  /* feature boxes */
  .features { position: absolute; left: 18px; top: 625px; width: 775px; display: flex; gap: 16px; }
  .feature { flex: 1; background: var(--green); border: 4px solid var(--white); border-radius: 14px;
    outline: 3px solid var(--green); color: var(--white); text-align: center; padding: 18px 12px;
    font-family: "Noto Sans JP", sans-serif; font-weight: 700; font-size: 22px; line-height: 1.5; height: 175px; white-space: nowrap; }
  .feature .em { color: var(--yellow); font-size: 30px; font-weight: 900; line-height: 1.35; }
  .feature .em-line { border-bottom: 3px solid var(--yellow); }

  /* set section */
  .sets { position: absolute; left: 0; top: 820px; width: 811px; height: 205px;
    background: linear-gradient(180deg, #ffffff 0%, var(--sky) 100%); }
  .set-badge { position: absolute; left: 18px; top: 10px; width: 190px; height: 190px; border-radius: 50%;
    background: var(--yellow); color: var(--green-dark); text-align: center; font-weight: 900; white-space: nowrap;
    display: flex; flex-direction: column; justify-content: center; line-height: 1.3; font-size: 18px; }
  .set-badge .big { font-size: 24px; color: var(--red); }
  .set-item { position: absolute; top: 18px; width: 160px; height: 150px; border-radius: 50%; }
  .set-hanami { left: 228px; background: radial-gradient(circle, #f7d1dc 0%, #d99ab0 60%, #9a6a7a 100%); }
  .set-star { left: 400px; background: radial-gradient(circle, #f2f4f6 0%, #9fa9b5 60%, #2c3a55 100%); }
  .set-sports { left: 572px; background: radial-gradient(circle, #f0d9b8 0%, #b99a6e 60%, #5f7d3a 100%); }
  .set-label { position: absolute; top: 160px; width: 160px; text-align: center; background: var(--green);
    color: var(--white); font-weight: 800; font-size: 18px; border-radius: 16px; padding: 4px 0; white-space: nowrap; }
  .set-etc { position: absolute; left: 745px; top: 165px; font-weight: 800; font-size: 20px; color: var(--green-dark); }

  /* recruit band */
  .recruit { position: absolute; left: 0; top: 1030px; width: 811px; height: 52px; background: var(--green);
    color: var(--white); text-align: center; font-weight: 900; font-size: 30px; line-height: 52px; white-space: nowrap; }

  /* footer */
  .footer { position: absolute; left: 0; top: 1082px; width: 811px; height: 118px; background: var(--white); }
  .brand { position: absolute; left: 30px; top: 20px; color: var(--green-dark); font-weight: 800; white-space: nowrap; }
  .brand .tag { font-size: 20px; display: block; }
  .brand .name { font-size: 48px; line-height: 1.1; }
  .contact { position: absolute; left: 410px; top: 16px; width: 380px; text-align: center; }
  .contact .lead { background: var(--green); color: var(--white); font-weight: 800; font-size: 24px;
    border-radius: 24px; padding: 6px 0; white-space: nowrap; }
  .contact .tel { display: flex; align-items: center; justify-content: center; gap: 6px; white-space: nowrap;
    color: var(--green-dark); font-weight: 900; font-size: 40px; line-height: 1.2; margin-top: 6px; }
  .contact .tel svg { width: 32px; height: 32px; flex: none; }
  .contact .tel small { font-size: 24px; align-self: flex-end; margin-bottom: 6px; }
</style>
</head>
<body>
<main class="card">
  <header class="header">
    <p class="price-line">年間<span class="amount">49,800</span>円<span class="course">スタンダードコース</span>で</p>
    <h1 class="headline"><span>みんなが喜ぶ福利厚生を実現!</span></h1>
  </header>

  <div class="photo photo-camp" role="img" aria-label="キャンプ場で楽しむ人たちの写真"></div>
  <div class="photo photo-climb" role="img" aria-label="雪山の山頂で登山を楽しむ人の写真"></div>
  <div class="photo photo-bbq" role="img" aria-label="バーベキューで肉を焼く写真"></div>

  <p class="bubble bubble-camp">キャンプも!</p>
  <p class="bubble bubble-bbq">バーベキューも!<small>他にもたくさん</small></p>
  <p class="bubble bubble-climb">本格登山も!</p>

  <h2 class="main-copy">遊び道具がいつでも<br>何回でもレンタルできちゃいます!</h2>

  <section class="features">
    <div class="feature">
      豊富なアウトドア用品を<br>月利用限度内まで<br>
      <span class="em"><span class="em-line">何回レンタルしても</span></span><br>
      <span class="em">一定額</span>のサービス!
    </div>
    <div class="feature">
      法人でご登録いただきますと、<br>
      <span class="em"><span class="em-line">社員の方全員</span></span>で<br>
      お使いいただけます。
    </div>
  </section>

  <section class="sets">
    <div class="set-badge">オリジナル<span class="big">まるごとセット</span>を沢山ご用意<br>しています!</div>
    <div class="set-item set-hanami" role="img" aria-label="お花見の写真"></div>
    <div class="set-item set-star" role="img" aria-label="天体望遠鏡の写真"></div>
    <div class="set-item set-sports" role="img" aria-label="運動会で走る子どもの写真"></div>
    <p class="set-label" style="left:228px">お花見セット</p>
    <p class="set-label" style="left:400px">天体観測セット</p>
    <p class="set-label" style="left:572px">運動会セット</p>
    <p class="set-etc">など</p>
  </section>

  <p class="recruit">アウトドア用品年間定額レンタル法人会員募集中!</p>

  <footer class="footer">
    <div class="brand"><span class="tag">遊びかた総合提案</span><span class="name">あおぞらの森</span></div>
    <div class="contact">
      <p class="lead">お問い合わせはお気軽に!</p>
      <p class="tel">
        <svg viewBox="0 0 24 24" aria-hidden="true"><path fill="currentColor" d="M6.6 10.8a15.1 15.1 0 0 0 6.6 6.6l2.2-2.2a1 1 0 0 1 1-.25 11.4 11.4 0 0 0 3.6.57 1 1 0 0 1 1 1V20a1 1 0 0 1-1 1A17 17 0 0 1 3 4a1 1 0 0 1 1-1h3.5a1 1 0 0 1 1 1c0 1.25.2 2.45.57 3.6a1 1 0 0 1-.25 1z"/></svg>
        <small>TEL.</small><span>0555-00-1234</span>
      </p>
    </div>
  </footer>
</main>
</body>
</html>
```